In home Senior Care Catalogue Brochure and Presentation Folder

*We are a non-medical home care company that helps seniors stay in their own homes by providing quality in home senior care. Please see website for better understanding: www.brightmeadowhelpers.com

We need our current print material redesigned and converted into an 6-8 page catalogue with all the necessary detailed information about our services. Would like the catalogue to read like a story:

1. Addressing the issue with emotions
and
2. Offering a solution (our services)
further explaining services, about us, testimonials, credentials, and how to get started with us. How easy it is to bring a caregiver in their loved ones home. And to GAIN THEIR TRUST.

This catalogue will be used to bring along to assessments when we are meeting the family. Or may be sent out to families when they want more information on care. But this packet will detail everything about us and what we do, and how we can help them. This catalogue will need to go in a designed presentation folder and/or maybe you can create a folder that can have the designed pages inserted like the example below.

1. I really like the idea of company folder attached (inspirational design)

Ideally either create a catalogue to put in an accompanied design folder, or be creative and create something like what is attached, where the quality pages can be inserted in the entire packet.

2. Testimonials can be pulled from our Rivlo page:
https://www.rivlo.com/biz/bright-meadow-helpers-newport-beach

3. Credentials: Add HCO License #: 518263940

4. Be sure to explain what Tendwise is and how the family can log in to view the schedule of the caregiving clocking in/out, etc.
https://www.tendwiseportal.com/family-room

Target Market(s)

65 and up. Male and female
Show compassion for what many adult children are going through — fear, confusion and feelings of guilt — when they can't provide a constant care for their aging parents. It is easier for potential clients to relate to an organization that understands their needs and challenges.

Industry/Entity Type

Health Care

Font styles to use
Serif

Requirements
Must have
• -Branding needs to match business card design as well as website design cues.
• -Needs to be FLAT DESIGN
• -Clean layout
• -Pictures of caregivers helping elderly (only where it is really needed)
Nice to have
• -Minimalistic but informative
• -Utilize infographics
• -Creative folder design with insertion of pages
• -One favorite idea is under 'Packet Ideas PM' name
• -Possibly an all Infographic design
Should not have
• -Cluttered/Messy

```html
<!DOCTYPE html>
<html lang="en">
<head>
<meta charset="utf-8">
<title>Bright Meadow Helpers – Presentation Folder and Inserts</title>
<link href="https://fonts.googleapis.com/css2?family=Montserrat:wght@300;400;500;600;700&display=swap" rel="stylesheet">
<style>
  :root {
    --bg: #808185;
    --white: #ffffff;
    --gold: #f5b13f;
    --green: #2a6a3a;
    --olive: #8c7a45;
    --ink: #333333;
    --muted: #9a9a9a;
    --label: #ffffff;
  }
  * { box-sizing: border-box; margin: 0; padding: 0; }
  html, body { width: 1200px; height: 1042px; overflow: hidden; background: var(--bg); }
  body { font-family: "Montserrat", sans-serif; color: var(--ink); position: relative; }

  .section-label {
    position: absolute; color: var(--label); font-weight: 600; font-size: 17px; letter-spacing: .5px;
  }
  .section-label--inserts { left: 748px; top: 134px; }
  .section-label--pocket { left: 562px; top: 978px; }

  .panel { position: absolute; background: var(--white); overflow: hidden; }
  .notch {
    position: absolute; top: -22px; width: 44px; height: 44px; border-radius: 50%; background: var(--bg);
  }

  /* Brand name set as text */
  .brand { display: flex; flex-direction: column; align-items: center; gap: 10px; }
  .brand__dot { width: 36px; height: 36px; border-radius: 50%; background: var(--olive); }
  .brand__name {
    color: var(--green); font-weight: 600; text-align: center; line-height: 1.05; letter-spacing: -.5px;
  }

  .band-gold { position: absolute; left: 0; right: 0; background: var(--gold); color: var(--white); }
  .band-green { position: absolute; left: 0; right: 0; background: var(--green); color: var(--white); }
  .tagline { text-align: center; font-weight: 300; line-height: 1.05; }
  .tagline strong { font-weight: 700; }
  .intro { text-align: center; font-size: 10px; line-height: 1.45; }
  .url { color: var(--gold); font-weight: 600; letter-spacing: 1.4px; text-align: center; }

  /* Front of folder */
  .folder-front { left: 68px; top: 80px; width: 514px; height: 398px; }
  .folder-front .brand { position: absolute; left: 0; right: 0; top: 118px; }
  .folder-front .brand__name { font-size: 42px; }
  .folder-front .band-gold { top: 256px; height: 64px; padding-top: 8px; }
  .folder-front .tagline { font-size: 22px; }
  .folder-front .band-green { top: 320px; bottom: 0; padding-top: 14px; }
  .folder-front .url { font-size: 11px; margin-top: 18px; }

  /* Insert */
  .insert { left: 624px; top: 168px; width: 540px; height: 332px; }
  .insert__icons { position: absolute; top: 22px; left: 0; right: 0; display: flex; justify-content: center; gap: 64px; }
  .credential { display: flex; flex-direction: column; align-items: center; width: 96px; }
  .credential__ring {
    width: 60px; height: 60px; border-radius: 50%; border: 3px solid var(--green);
    display: flex; align-items: center; justify-content: center;
  }
  .credential__fill { width: 34px; height: 34px; border-radius: 50%; }
  .credential__label { margin-top: 8px; font-size: 9px; font-weight: 600; text-align: center; color: #555; line-height: 1.2; }
  .insert__callout {
    position: absolute; left: 30px; right: 30px; top: 146px; height: 40px; border-radius: 10px;
    background: var(--gold); color: var(--green); font-size: 9.5px; font-weight: 700;
    display: flex; align-items: center; justify-content: center; text-align: center; padding: 0 20px; line-height: 1.3;
  }
  .insert__body { position: absolute; left: 40px; right: 40px; top: 198px; font-size: 7.6px; line-height: 1.45; text-align: center; color: #444; }
  .insert__body p + p { margin-top: 6px; }
  .insert__stripe { position: absolute; left: 0; right: 0; bottom: 34px; height: 6px; background: var(--gold); }
  .insert .band-green { bottom: 0; height: 34px; display: flex; align-items: center; justify-content: center; }
  .insert .url { font-size: 11px; }

  /* Pocket spread */
  .pocket { left: 51px; top: 535px; width: 1088px; height: 420px; }
  .pocket__fold { position: absolute; left: 544px; top: 0; bottom: 0; width: 1px; background: #dcdcdc; z-index: 2; }
  .pocket__back { position: absolute; left: 0; top: 0; width: 544px; height: 100%; }
  .pocket__cover { position: absolute; left: 545px; top: 0; width: 543px; height: 100%; }

  .pocket__back .brand { position: absolute; left: 46px; width: 200px; top: 110px; }
  .pocket__back .brand__dot { width: 26px; height: 26px; }
  .pocket__back .brand__name { font-size: 26px; }

  .testimonial { position: absolute; left: 308px; top: 94px; display: flex; gap: 14px; }
  .testimonial__who { width: 58px; display: flex; flex-direction: column; align-items: center; }
  .testimonial__photo { width: 54px; height: 54px; border-radius: 50%; background: radial-gradient(circle at 50% 40%, #f1d9c4, #d9b48c); }
  .testimonial__name { margin-top: 8px; font-size: 10px; font-weight: 700; color: var(--green); align-self: flex-start; }
  .testimonial__place { font-size: 8.5px; color: var(--green); align-self: flex-start; line-height: 1.3; }
  .testimonial__quote { width: 130px; font-size: 10px; line-height: 1.25; color: #333; }
  .testimonial__mark { font-size: 24px; color: #bcbcbc; font-weight: 700; line-height: 1; height: 18px; }

  .pocket__back .band-gold { top: 269px; height: 68px; }
  .contact { position: absolute; left: 62px; top: 12px; font-size: 10px; line-height: 1.3; color: #333; }
  .phone { position: absolute; left: 302px; top: 32px; font-size: 25px; font-weight: 700; color: var(--green); }
  .badge-24 {
    position: absolute; left: 372px; top: -24px; width: 44px; height: 44px; border-radius: 50%;
    background: var(--white); border: 3px solid var(--green); display: flex; align-items: center; justify-content: center;
  }
  .pocket__back .band-green { top: 337px; bottom: 0; padding-top: 36px; }
  .pocket__back .url { font-size: 12px; }
  .license { text-align: center; font-size: 9px; font-weight: 600; letter-spacing: 1px; }

  .pocket__cover .brand { position: absolute; left: 0; right: 0; top: 100px; }
  .pocket__cover .brand__dot { width: 40px; height: 40px; }
  .pocket__cover .brand__name { font-size: 46px; }
  .pocket__cover .band-gold { top: 269px; height: 68px; padding-top: 9px; }
  .pocket__cover .tagline { font-size: 25px; }
  .pocket__cover .band-green { top: 337px; bottom: 0; padding-top: 14px; }
  .pocket__cover .url { font-size: 12px; margin-top: 18px; }
</style>
</head>
<body>

  <!-- Folder front -->
  <section class="panel folder-front">
    <span class="notch" style="left:234px"></span>
    <div class="brand">
      <span class="brand__dot"></span>
      <span class="brand__name">Bright Meadow<br>Helpers</span>
    </div>
    <div class="band-gold">
      <p class="tagline">Outstanding <strong>Home Care and</strong><br><strong>Companionship</strong> for Seniors</p>
    </div>
    <div class="band-green">
      <p class="intro">Bright Meadow Helpers provides trained, certified, hands-on home care with a focus on respect,<br>trust and compatibility. We build positive care experiences for your loved ones and our staff alike.</p>
      <p class="url">www.brightmeadowhelpers.com</p>
    </div>
  </section>

  <span class="section-label section-label--inserts">INSERTS</span>

  <!-- Insert -->
  <section class="panel insert">
    <div class="insert__icons">
      <div class="credential">
        <div class="credential__ring">
          <svg width="34" height="34" viewBox="0 0 34 34" aria-hidden="true"><path d="M6 18 L14 27 L29 6" fill="none" stroke="#3c7fc9" stroke-width="5" stroke-linecap="round" stroke-linejoin="round"/></svg>
        </div>
        <span class="credential__label">Licensed, Bonded<br>and Insured</span>
      </div>
      <div class="credential">
        <div class="credential__ring"><span class="credential__fill" style="background:var(--gold)"></span></div>
        <span class="credential__label">Trained and<br>Certified Staff</span>
      </div>
      <div class="credential">
        <div class="credential__ring"><span class="credential__fill" style="background:#e03a3a"></span></div>
        <span class="credential__label">Care with Compassion<br>and Respect</span>
      </div>
    </div>
    <div class="insert__callout">At Bright Meadow Helpers, we don't just provide in home care, we provide fast, reliable, hands-on care with a guaranteed caregiver you will love.</div>
    <div class="insert__body">
      <p>We are dedicated to providing personable, hands-on, and integrated caring services that aim to help people maintain safe and comfortable life standards within the familiar settings of the home. The company is the brainchild of Daniel Whitford, who became passionate about the home care industry after witnessing its value first hand, caring for his grandmother and appreciating the value of quality care received within the domestic environment. Sadly, his beloved grandmother was later transferred to a nursing home beyond his control. There, she received substandard care, passing away shortly thereafter. His firsthand experience is a catalyst for his commitment to helping elderly people enjoy great quality care within their own homes for as long as possible.</p>
      <p>We treat each client and caregiver match, as if they were my own family member, if I would place that caregiver with my loved one.</p>
    </div>
    <div class="insert__stripe"></div>
    <div class="band-green"><p class="url">www.brightmeadowhelpers.com</p></div>
  </section>

  <!-- Pocket spread -->
  <section class="panel pocket">
    <span class="notch" style="left:302px"></span>
    <span class="pocket__fold"></span>

    <div class="pocket__back">
      <div class="brand">
        <span class="brand__dot"></span>
        <span class="brand__name">Bright Meadow<br>Helpers</span>
      </div>

      <div class="testimonial">
        <div class="testimonial__who">
          <span class="testimonial__photo" role="img" aria-label="Portrait photo of the client giving the testimonial"></span>
          <span class="testimonial__name">Maren T.</span>
          <span class="testimonial__place">Newport<br>Beach, Ca</span>
        </div>
        <div class="testimonial__quote">
          <div class="testimonial__mark">&ldquo;</div>
          Not just your normal care-giving agency, they are not a big "machine" but take extra care to find the best situation for your loved one.
        </div>
      </div>

      <div class="band-gold">
        <div class="badge-24">
          <svg width="28" height="28" viewBox="0 0 28 28" aria-hidden="true">
            <circle cx="14" cy="14" r="11" fill="none" stroke="#f5b13f" stroke-width="2.5"/>
            <text x="14" y="18" text-anchor="middle" font-family="Montserrat, sans-serif" font-size="10" font-weight="700" fill="#f5b13f">24</text>
          </svg>
        </div>
        <p class="contact">Serving Newport Beach and surrounding area<br>12 Harbor View Ct<br>Suite 210<br>Newport Beach, CA 92660</p>
        <p class="phone">(949) 555-0182</p>
      </div>
      <div class="band-green">
        <p class="url">www.brightmeadowhelpers.com</p>
        <p class="license">HCO License #: 518263940</p>
      </div>
    </div>

    <div class="pocket__cover">
      <div class="brand">
        <span class="brand__dot"></span>
        <span class="brand__name">Bright Meadow<br>Helpers</span>
      </div>
      <div class="band-gold">
        <p class="tagline">Outstanding <strong>Home Care and</strong><br><strong>Companionship</strong> for Seniors</p>
      </div>
      <div class="band-green">
        <p class="intro">Bright Meadow Helpers provides trained, certified, hands-on home care with a focus on respect,<br>trust and compatibility. We build positive care experiences for your loved ones and our staff alike.</p>
        <p class="url">www.brightmeadowhelpers.com</p>
      </div>
    </div>
  </section>

  <span class="section-label section-label--pocket">POCKET</span>

</body>
</html>
```